Kestrel Lane flyer

Need a A6 size horizontal layout flyer. See attached example for ideas as well as some images I have which you can use. we are a hire car company that provides vehicles to clients who have recently been involved in car accidents and who's cars are currently getting fixed and so they lose the use of their own vehicle. see our website to keep flyer in line with website and for any further information kestrellane.com.au

Target Market(s)

people involved in not at fault car accidents

Industry/Entity Type

It Company

Requirements
Must have
• *ask people to let us know where they got our flyer from when they call us
• *call to action for people to call our phone number 1800 417 582
Should not have
• any mentioning that the vehicle is free

```html
<!DOCTYPE html>
<html lang="en">
<head>
<meta charset="utf-8">
<title>Kestrel Lane – Accident Replacement Car Flyer</title>
<link rel="stylesheet" href="https://fonts.googleapis.com/css2?family=Archivo+Black&family=Arimo:wght@400;700&family=Roboto+Condensed:wght@300;400&display=swap">
<style>
  :root {
    --ink: #111111;
    --white: #ffffff;
    --brand-blue: #3d9bf5;
    --deep-blue: #1f78d6;
    --sky-blue: #5aaef4;
    --sun-yellow: #f5b700;
    --panel-grey: #e2e2e2;
    --accent-red: #c8104f;
  }
  * { box-sizing: border-box; margin: 0; padding: 0; }
  html, body { width: 1200px; height: 848px; overflow: hidden; background: var(--white); }
  .flyer { position: relative; width: 1200px; height: 848px; background: var(--white); font-family: "Arimo", Arial, sans-serif; color: var(--ink); }

  .photo { position: absolute; top: 0; height: 392px; }
  .photo--car { left: 0; width: 517px; background: linear-gradient(120deg, #3d3a2e 0%, #8c8a80 35%, #e8e9eb 60%, #b9bcc0 100%); }
  .photo--drivers { left: 517px; width: 683px; background: linear-gradient(100deg, #4b4f57 0%, #c9c6c0 35%, #e9e4dc 55%, #9fb6cc 80%, #7a3a44 100%); }

  .brand-block { position: absolute; left: 84px; top: 329px; width: 1031px; height: 212px; background: var(--ink); }
  .brand-name { position: absolute; left: 84px; top: 329px; width: 215px; height: 212px; display: flex; align-items: center; justify-content: center; color: var(--white); font-family: "Archivo Black", sans-serif; font-size: 25px; letter-spacing: 0.5px; }

  .offer { position: absolute; left: 299px; top: 331px; width: 816px; height: 189px; background: var(--brand-blue); color: var(--white); text-align: center; }
  .offer__title { position: absolute; left: 0; right: 0; top: 28px; font-family: "Archivo Black", sans-serif; font-size: 45px; line-height: 1; letter-spacing: 0.5px; }
  .offer__perks { position: absolute; left: 0; right: 0; top: 88px; display: flex; justify-content: center; gap: 34px; font-size: 31px; line-height: 1; }
  .perk { display: flex; align-items: center; gap: 4px; }
  .perk svg { width: 30px; height: 30px; }
  .offer__rule { position: absolute; left: 10px; right: 16px; top: 136px; height: 2px; background: var(--white); }
  .offer__strap { position: absolute; left: 0; right: 0; top: 150px; font-family: "Roboto Condensed", sans-serif; font-weight: 300; font-size: 21px; letter-spacing: -0.3px; }

  .steps-heading { position: absolute; left: 90px; top: 553px; width: 545px; text-align: center; font-family: "Archivo Black", sans-serif; font-size: 21.5px; line-height: 28px; letter-spacing: 0.6px; }
  .step { position: absolute; top: 617px; width: 200px; text-align: center; font-size: 19px; line-height: 24px; }
  .step__icon { display: block; width: 113px; height: 113px; margin: 0 auto 32px; }
  .step--apply { left: 63px; }
  .step--details { left: 224px; }
  .step--vehicle { left: 406px; width: 240px; }
  .step strong { font-weight: 700; }
  .step small { display: block; font-size: 12px; line-height: 14px; }

  .contact { position: absolute; left: 678px; top: 563px; width: 436px; height: 144px; background: var(--panel-grey); }
  .contact__item { position: absolute; top: 10px; text-align: center; font-weight: 700; font-size: 25px; line-height: 26px; }
  .contact__item svg { display: block; width: 66px; height: 66px; margin: 0 auto 8px; }
  .contact__item--phone { left: 6px; width: 176px; }
  .contact__item--web { left: 190px; width: 240px; }

  .about { position: absolute; left: 678px; top: 716px; width: 436px; }
  .about__title { font-weight: 700; font-size: 19px; line-height: 22px; }
  .about__title span { color: var(--accent-red); }
  .about__text { margin-top: 12px; font-size: 10.5px; line-height: 17px; }
</style>
</head>
<body>
<main class="flyer">
  <div class="photo photo--car" role="img" aria-label="Photo of the front of a white car parked on a shaded road"></div>
  <div class="photo photo--drivers" role="img" aria-label="Photo of a smiling couple seated in a car, the man driving"></div>

  <div class="brand-block"></div>
  <div class="brand-name">Kestrel Lane</div>

  <section class="offer">
    <h1 class="offer__title">ACCIDENT REPLACEMENT CAR</h1>
    <div class="offer__perks">
      <span class="perk"><svg viewBox="0 0 30 30"><rect x="3" y="6" width="20" height="20" fill="none" stroke="#f5b700" stroke-width="2.5"/><path d="M7 15l5 6L27 3" fill="none" stroke="#f5b700" stroke-width="3"/></svg>Free Advice</span>
      <span class="perk"><svg viewBox="0 0 30 30"><rect x="3" y="6" width="20" height="20" fill="none" stroke="#f5b700" stroke-width="2.5"/><path d="M7 15l5 6L27 3" fill="none" stroke="#f5b700" stroke-width="3"/></svg>Excess Waiver Included</span>
    </div>
    <div class="offer__rule"></div>
    <p class="offer__strap">WE GET DRIVERS BACK ON THE ROAD AFTER CAR ACCIDENTS EVERYDAY</p>
  </section>

  <h2 class="steps-heading">ARRANGING AN ACCIDENT REPLACEMENT VEHICLE FOR YOURSELF IS EASY AS 1,2,3</h2>

  <div class="step step--apply">
    <svg class="step__icon" viewBox="0 0 113 113">
      <circle cx="56.5" cy="56.5" r="56.5" fill="var(--sun-yellow)"/>
      <rect x="30" y="30" width="44" height="52" fill="none" stroke="#111" stroke-width="5"/>
      <path d="M38 45h20M38 56h16M38 67h12" stroke="#111" stroke-width="4"/>
      <path d="M52 74l26-32 7 6-26 32-10 4z" fill="#111"/>
    </svg>
    APPLY ONLINE<br>OR CALL<br><strong>1800 417 582</strong>
  </div>

  <div class="step step--details">
    <svg class="step__icon" viewBox="0 0 113 113">
      <circle cx="56.5" cy="56.5" r="56.5" fill="var(--sky-blue)"/>
      <rect x="44" y="22" width="34" height="62" rx="5" fill="#fff"/>
      <rect x="48" y="30" width="26" height="44" fill="var(--sky-blue)"/>
      <path d="M20 66l24-6 6 22-24 6z" fill="#fff"/>
      <path d="M20 66l16 8 8-14" fill="none" stroke="var(--sky-blue)" stroke-width="2"/>
    </svg>
    PROVIDE<br>ACCIDENT<br>DETAILS
  </div>

  <div class="step step--vehicle">
    <svg class="step__icon" viewBox="0 0 113 113">
      <circle cx="56.5" cy="56.5" r="56.5" fill="var(--deep-blue)"/>
      <path d="M14 66v-10l10-2 8-14h44l10 14 12 2v10z" fill="#fff"/>
      <path d="M36 43h16v11H30zM56 43h16l6 11H56z" fill="var(--deep-blue)"/>
      <circle cx="32" cy="68" r="7" fill="#fff" stroke="var(--deep-blue)" stroke-width="3"/>
      <circle cx="82" cy="68" r="7" fill="#fff" stroke="var(--deep-blue)" stroke-width="3"/>
    </svg>
    YOU GET A<br>REPLACEMENT VEHICLE
    <small>(WE TAKE CARE OF THE REST)</small>
  </div>

  <section class="contact">
    <div class="contact__item contact__item--phone">
      <svg viewBox="0 0 66 66"><circle cx="33" cy="33" r="30" fill="#fff" stroke="#111" stroke-width="3"/><path d="M22 16c-4 3-6 8-3 15 4 9 9 15 17 19 6 3 10 1 13-3l-7-7-5 3c-5-3-8-7-10-12l4-4z" fill="#111"/></svg>
      1800417582
    </div>
    <div class="contact__item contact__item--web">
      <svg viewBox="0 0 66 66"><circle cx="33" cy="33" r="30" fill="#fff" stroke="#111" stroke-width="3"/><path d="M14 27l30-10 8 22-30 10z" fill="#fff" stroke="#111" stroke-width="3"/><path d="M14 27l22 6 8-16M22 49l10-14M52 39l-16-6" fill="none" stroke="#111" stroke-width="2.5"/></svg>
      kestrellane<br>.com.au
    </div>
  </section>

  <section class="about">
    <h3 class="about__title"><span>ABOUT</span> US</h3>
    <p class="about__text">
      Our local team helps drivers stay mobile after road accidents.<br>
      We arrange a suitable hire vehicle while your car is repaired.<br>
      When you call, please tell us where you found this flyer today.<br>
      Friendly support from first call until your own car returns.
    </p>
  </section>
</main>
</body>
</html>
```